Plumbing & Heating company

A leaflet containing -

Company name - Bellfield Plumbing Solutions
logo
Mobile number - 07700 900412
Landline - 01632 960718
Email - Info@bellfieldplumbing.example.co.uk
website - Bellfield-plumbing.example.co.uk
Social media logos - insta, Facebook

services we offer

- Boiler replacements (free quote)
- General plumbing & heating
- Tap replacements
- 1st & 2nd
- New builds & Extensions
- Cylinder replcemets

```html
<!DOCTYPE html>
<html lang="en">
<head>
<meta charset="utf-8">
<title>Bellfield Plumbing Solutions – Leaflet</title>
<link href="https://fonts.googleapis.com/css2?family=Poppins:wght@400;500;600;700;800&display=swap" rel="stylesheet">
<style>
  :root {
    --page: #ececec;
    --charcoal: #333236;
    --blue: #2a9bd7;
    --orange: #f0703a;
    --purple: #3f3a8c;
    --white: #ffffff;
    --gold: #c99a2e;
    --ink: #2b2b2b;
  }
  * { box-sizing: border-box; margin: 0; padding: 0; }
  html, body { width: 766px; height: 1200px; overflow: hidden; background: var(--page); font-family: "Poppins", sans-serif; }
  .leaflet {
    position: absolute; left: 23px; top: 134px; width: 720px; height: 931px;
    background: var(--charcoal); overflow: hidden; box-shadow: 0 14px 30px rgba(0,0,0,.25);
  }
  .hero-photo {
    position: absolute; left: 0; top: 0; width: 720px; height: 436px;
    background: linear-gradient(90deg, var(--charcoal) 0%, var(--charcoal) 38%, #4a4e5a 58%, #6d7684 78%, #8b96a3 100%);
  }
  .brand {
    position: absolute; left: 37px; top: 70px; width: 300px;
    display: flex; align-items: center; justify-content: center; gap: 8px;
  }
  .brand-mark { width: 14px; height: 14px; border-radius: 50%; background: var(--orange); flex: none; }
  .brand-name { font-weight: 700; font-size: 19px; color: var(--blue); line-height: 1.1; }
  .kicker {
    position: absolute; left: 37px; top: 159px; width: 300px; display: flex; align-items: center; justify-content: center; gap: 10px;
    color: var(--white); font-weight: 700; font-size: 20px;
  }
  .kicker::before, .kicker::after { content: ""; width: 36px; height: 3px; background: var(--orange); }
  .headline { position: absolute; left: 40px; top: 182px; width: 300px; font-weight: 800; line-height: .86; }
  .headline .line-system { display: block; font-size: 66px; color: var(--blue); }
  .headline .line-design { display: block; font-size: 66px; color: var(--orange); }
  .headline .line-install { display: block; font-size: 32px; color: var(--blue); margin-top: 8px; line-height: 1; }
  .intro { position: absolute; left: 37px; top: 355px; width: 345px; color: var(--white); font-size: 13px; line-height: 1.18; }
  .band { position: absolute; left: 0; width: 720px; background: var(--orange); color: var(--white); font-weight: 700; }
  .band-services { top: 436px; height: 48px; font-size: 28px; text-align: center; line-height: 48px; }
  .services { position: absolute; left: 0; top: 484px; width: 720px; height: 200px; background: var(--purple); }
  .service { position: absolute; display: flex; align-items: flex-start; gap: 12px; color: var(--white); font-weight: 500; font-size: 21px; line-height: 1.06; }
  .service svg { flex: none; margin-top: -3px; }
  .certs { position: absolute; left: 0; top: 684px; width: 720px; height: 123px; background: var(--white); }
  .cert-badge { position: absolute; top: 14px; height: 28px; }
  .cert-text { position: absolute; left: 40px; top: 50px; width: 330px; font-size: 10px; line-height: 1.25; color: var(--ink); }
  .cert-text .accent { color: var(--orange); }
  .work-photo { position: absolute; top: 22px; width: 92px; height: 92px; border-radius: 50%; border: 4px solid var(--orange); background: radial-gradient(circle, #d8d2c6 0%, #a8947a 100%); }
  .band-cta { top: 807px; height: 33px; font-size: 18px; line-height: 33px; padding-left: 34px; }
  .contact { position: absolute; top: 840px; left: 0; width: 720px; height: 91px; }
  .phone-icon { position: absolute; left: 33px; top: 14px; }
  .contact-col { position: absolute; top: 6px; color: var(--white); white-space: nowrap; }
  .contact-col .number { font-weight: 700; font-size: 26px; color: var(--blue); line-height: 1.2; }
  .contact-col .detail { font-size: 11.5px; line-height: 1.35; }
  .contact-col .small { font-size: 10px; font-weight: 600; }
  .divider { position: absolute; left: 321px; top: 14px; width: 2px; height: 60px; background: var(--blue); }
  .social { display: flex; align-items: center; gap: 5px; }
  .social i { display: inline-block; width: 11px; height: 11px; border-radius: 2px; background: var(--orange); }
  .social i + i { background: var(--blue); }
  .guarantee { position: absolute; left: 610px; top: -28px; }
</style>
</head>
<body>
<main class="leaflet">
  <div class="hero-photo" role="img" aria-label="Plumber in a hard hat tightening pipework fittings with an adjustable wrench"></div>

  <div class="brand"><span class="brand-mark"></span><span class="brand-name">Bellfield Plumbing Solutions</span></div>

  <div class="kicker">PROFESSIONAL</div>
  <h1 class="headline">
    <span class="line-system">SYSTEM</span>
    <span class="line-design">DESIGN</span>
    <span class="line-install">&amp; INSTALLATION</span>
  </h1>
  <p class="intro">We are specialists in System design &amp; installation – 1st &amp; 2nd fix, and have a considerable experience in both new build and refurbishment projects including domestic, commercial and listed properties.</p>

  <div class="band band-services">OUR SERVICES</div>

  <section class="services">
    <div class="service" style="left:34px;top:22px">
      <svg width="32" height="32" viewBox="0 0 32 32"><circle cx="16" cy="16" r="14" fill="#fff" stroke="#f0703a" stroke-width="3"/><rect x="12" y="9" width="8" height="14" rx="1.5" fill="none" stroke="#3f3a8c" stroke-width="1.6"/><circle cx="16" cy="17" r="2" fill="#f0703a"/></svg>
      <span>Boiler Replacements<br>(Free Quote)</span>
    </div>
    <div class="service" style="left:34px;top:80px">
      <svg width="32" height="32" viewBox="0 0 32 32"><circle cx="16" cy="16" r="14" fill="#fff" stroke="#f0703a" stroke-width="3"/><path d="M16 8c-3 4-5 6-5 9a5 5 0 0 0 10 0c0-3-2-5-5-9z" fill="none" stroke="#3f3a8c" stroke-width="1.6"/></svg>
      <span>General Plumbing &amp;<br>Heating</span>
    </div>
    <div class="service" style="left:34px;top:138px">
      <svg width="32" height="32" viewBox="0 0 32 32"><circle cx="16" cy="16" r="14" fill="#fff" stroke="#f0703a" stroke-width="3"/><path d="M9 14h10v4M14 14v-4M11 10h6M19 21v2" fill="none" stroke="#3f3a8c" stroke-width="1.8" stroke-linecap="round"/></svg>
      <span>Tap Replacements</span>
    </div>
    <div class="service" style="left:404px;top:22px">
      <svg width="32" height="32" viewBox="0 0 32 32"><circle cx="16" cy="16" r="14" fill="#fff" stroke="#f0703a" stroke-width="3"/><path d="M11 9v14M21 9v14M11 13h4M17 19h4" fill="none" stroke="#3f3a8c" stroke-width="1.8" stroke-linecap="round"/></svg>
      <span>1st &amp; 2nd Fix</span>
    </div>
    <div class="service" style="left:404px;top:80px">
      <svg width="32" height="32" viewBox="0 0 32 32"><circle cx="16" cy="16" r="14" fill="#fff" stroke="#f0703a" stroke-width="3"/><path d="M9 16l7-6 7 6M11 15v8h10v-8" fill="none" stroke="#3f3a8c" stroke-width="1.8" stroke-linejoin="round"/></svg>
      <span>New Builds &amp;<br>Extensions</span>
    </div>
    <div class="service" style="left:404px;top:138px">
      <svg width="32" height="32" viewBox="0 0 32 32"><circle cx="16" cy="16" r="14" fill="#fff" stroke="#f0703a" stroke-width="3"/><rect x="11" y="8" width="4" height="16" rx="2" fill="none" stroke="#3f3a8c" stroke-width="1.6"/><rect x="17" y="8" width="4" height="16" rx="2" fill="none" stroke="#3f3a8c" stroke-width="1.6"/></svg>
      <span>Cylinder<br>Replcements</span>
    </div>
  </section>

  <section class="certs">
    <div class="cert-badge" style="left:40px;width:68px;background:#2b3f66"></div>
    <div class="cert-badge" style="left:117px;top:6px;width:46px;height:38px;border:1px solid #4a8a6a;background:#f3f7f2"></div>
    <p class="cert-text">We offer a wide range of services covering Winchester and the surrounding areas.<br>We are Gas registered and fully ensured.<br><span class="accent">We are registered with the National Gas Register (4417203) and a Harlow Approved Installer</span></p>
    <div class="work-photo" role="img" aria-label="Installed wall-mounted boiler" style="left:392px"></div>
    <div class="work-photo" role="img" aria-label="Copper pipework manifold" style="left:500px"></div>
    <div class="work-photo" role="img" aria-label="Hot water cylinder installation" style="left:608px"></div>
  </section>

  <div class="band band-cta">CONTACT US TODAY TO GET A FREE QUOTE</div>

  <section class="contact">
    <svg class="phone-icon" width="34" height="44" viewBox="0 0 34 44"><rect x="8" y="2" width="22" height="40" rx="4" fill="#2a9bd7"/><rect x="11" y="7" width="16" height="26" fill="#1d6f9d"/><circle cx="19" cy="37" r="2" fill="#fff"/><path d="M2 18h10v10H2z" fill="#2a9bd7"/></svg>
    <div class="contact-col" style="left:88px">
      <div class="number">07700 900412</div>
      <div class="detail">Info@bellfieldplumbing.example.co.uk</div>
      <div class="small">Open Monday - Sunday 24-Hours</div>
    </div>
    <div class="divider"></div>
    <div class="contact-col" style="left:340px">
      <div class="number">01632 960718</div>
      <div class="detail">www.bellfield-plumbing.example.co.uk</div>
      <div class="detail social"><i></i><i></i>&nbsp;bellfield-plumbing</div>
    </div>
    <svg class="guarantee" width="100" height="100" viewBox="0 0 104 104" role="img" aria-label="Satisfaction guarantee seal">
      <circle cx="52" cy="52" r="48" fill="#c99a2e"/>
      <circle cx="52" cy="52" r="38" fill="#2a2a2a" stroke="#e8c35a" stroke-width="3"/>
      <rect x="4" y="54" width="96" height="16" fill="#d9aa3a"/>
    </svg>
  </section>
</main>
</body>
</html>
```